ashby paving works

Needs to have phone number 0412885107 and email marklowry@pavemail.com.au.
ABN 27613048852
name mark lowry

For all your concreting solutions
Excavation
Exposed & colour concrete
House & shed slabs
Driveways
Landing & steps

Contact Information for Business Card

ph 0412885107
email marklowry@pavemail.com.au.
ABN 27613048852
name mark lowry

```html
<!DOCTYPE html>
<html lang="en">
<head>
<meta charset="utf-8">
<title>Ashby Paving Works – Business Card</title>
<link href="https://fonts.googleapis.com/css2?family=Lato:wght@400;700&display=swap" rel="stylesheet">
<style>
  :root {
    --backdrop: #2f2f30;
    --orange: #f26a23;
    --slate: #626262;
    --white: #ffffff;
    --card-shadow: 0 3px 8px rgba(0,0,0,.55);
  }
  html, body {
    margin: 0;
    width: 1200px;
    height: 802px;
    overflow: hidden;
    background: var(--backdrop);
    font-family: "Lato", sans-serif;
  }
  .card {
    position: absolute;
    top: 274px;
    width: 442px;
    height: 264px;
    box-shadow: var(--card-shadow);
    overflow: hidden;
  }
  .card--front { left: 136px; background: var(--orange); }
  .card--back { left: 624px; background: var(--white); }

  .front-panel { position: absolute; inset: 0; }

  .front-brand {
    position: absolute;
    left: 52px;
    top: 122px;
    margin: 0;
    color: var(--orange);
    font-weight: 700;
    font-size: 23px;
    letter-spacing: .5px;
    text-transform: uppercase;
  }
  .front-details {
    position: absolute;
    right: 25px;
    top: 26px;
    text-align: right;
    color: var(--white);
  }
  .holder-name {
    margin: 0 0 10px;
    font-weight: 700;
    font-size: 17px;
    text-transform: uppercase;
  }
  .contact-line { margin: 0 0 4px; font-size: 12.5px; }

  .front-services {
    position: absolute;
    right: 26px;
    top: 168px;
    text-align: right;
    color: var(--white);
  }
  .tagline {
    margin: 0 0 5px;
    font-size: 10.5px;
    line-height: 14px;
    text-transform: uppercase;
  }
  .service-line { margin: 0; font-size: 12.5px; line-height: 16px; }

  .back-mark {
    position: absolute;
    left: 82px;
    top: 104px;
    width: 56px;
    height: 56px;
    background: var(--orange);
  }
  .back-divider {
    position: absolute;
    left: 162px;
    top: 92px;
    width: 1.5px;
    height: 81px;
    background: var(--orange);
  }
  .back-brand {
    position: absolute;
    left: 171px;
    top: 106px;
    margin: 0;
    color: var(--orange);
    font-weight: 700;
    font-size: 18px;
    text-transform: uppercase;
    letter-spacing: .3px;
  }
  .back-phone {
    position: absolute;
    left: 171px;
    top: 135px;
    margin: 0;
    color: var(--orange);
    font-size: 14px;
    letter-spacing: 2.5px;
  }
</style>
</head>
<body>
  <section class="card card--front">
    <svg class="front-panel" width="442" height="264" viewBox="0 0 442 264" aria-hidden="true">
      <polygon points="131,0 442,0 442,264 131,264 0,131" fill="var(--slate)"/>
    </svg>
    <p class="front-brand">Ashby Paving Works</p>
    <div class="front-details">
      <p class="holder-name">Mark Lowry</p>
      <p class="contact-line">ABN 27613048852</p>
      <p class="contact-line">marklowry@pavemail.com.au</p>
    </div>
    <div class="front-services">
      <p class="tagline">For all your concreting<br>solutions</p>
      <p class="service-line">Excavation &nbsp;| Landing &amp; step</p>
      <p class="service-line">House &amp; shed slabs &nbsp;| &nbsp;Driveways</p>
      <p class="service-line">Exposed &amp; colour concrete</p>
    </div>
  </section>

  <section class="card card--back">
    <div class="back-mark"></div>
    <div class="back-divider"></div>
    <p class="back-brand">Ashby Paving Works</p>
    <p class="back-phone">0412885107</p>
  </section>
</body>
</html>
```